Portal Panel Medic need professional looking business card printed on plastic, Commericial, Industri

We are family owned and operated garage door company in Indianapolis, Indiana. We sale service and install dock equipment, doors, operators. We are looking to expand our commercial/ industrial division. We also service all residential doors and operators. We are looking for a business that stands out of the crowd. We are committed to have the best customer service in the industry.

Target Market(s)

National and local general contractors, National/ Corpate service accounts,

Industry/Entity Type

Business Service

Contact Information for Business Card

To be printed on plastic stock

Font styles to use
Sans Serif

Colors
ffffff
f04a50
ec1f27

Requirements
Must have
• Name, website,email, phone number, position.
Nice to have
• A standout professional design

```html
<!DOCTYPE html>
<html lang="en">
<head>
<meta charset="utf-8">
<title>Portal Panel Medic – Business Card</title>
<link href="https://fonts.googleapis.com/css2?family=Open+Sans:ital,wght@0,400;0,700;1,700&display=swap" rel="stylesheet">
<style>
  :root {
    --brand-red: #ec2c35;
    --accent-red: #ec1f27;
    --white: #ffffff;
    --ink: #2b2b2b;
    --text-grey: #555555;
    --rule-grey: #9a9a9a;
    --backdrop: #3c3c3c;
    --art-tone: #b9a79a;
  }
  * { box-sizing: border-box; margin: 0; padding: 0; }
  html, body { width: 1200px; height: 801px; overflow: hidden; }
  body {
    background: var(--backdrop);
    font-family: "Open Sans", Arial, sans-serif;
    position: relative;
  }
  .card {
    position: absolute;
    top: 260px;
    width: 494px;
    height: 282px;
    border-radius: 10px;
    overflow: hidden;
  }
  .card--front { left: 89px; background: var(--brand-red); }
  .card--back { left: 649px; background: var(--white); }

  .mascot-art {
    position: absolute;
    border-radius: 6px;
    background: linear-gradient(160deg, #e8e2dc 0%, var(--art-tone) 60%, #6b4a34 100%);
  }
  .card--front .mascot-art { left: 94px; top: 66px; width: 62px; height: 148px; }
  .card--back .mascot-art { left: 129px; top: 30px; width: 50px; height: 120px; }

  .brand-name {
    position: absolute;
    font-weight: 700;
    white-space: nowrap;
    line-height: 1;
  }
  .card--front .brand-name {
    left: 170px; top: 124px;
    font-size: 30px;
    color: var(--white);
  }
  .card--back .brand-name {
    left: 192px; top: 78px;
    font-size: 24px;
    color: var(--accent-red);
  }

  .tagline-band {
    position: absolute;
    left: 0; top: 228px;
    width: 100%; height: 28px;
    background: var(--white);
    display: flex; align-items: center; justify-content: center;
  }
  .tagline {
    font-style: italic;
    font-weight: 700;
    font-size: 15.5px;
    color: var(--ink);
  }

  .divider {
    position: absolute;
    left: 25px; top: 186px;
    width: 456px; height: 3px;
    background: var(--rule-grey);
  }
  .person {
    position: absolute;
    left: 61px; top: 196px;
    color: var(--text-grey);
  }
  .person__name { font-size: 19px; font-weight: 700; line-height: 1.2; }
  .person__role { font-size: 14px; font-weight: 400; margin-top: 2px; }

  .contact-list {
    position: absolute;
    left: 311px; top: 198px;
    list-style: none;
    color: var(--text-grey);
    font-size: 14px;
  }
  .contact-list li {
    display: flex; align-items: center; gap: 9px;
    height: 20px;
  }
  .contact-list svg { width: 14px; height: 14px; flex: none; }
</style>
</head>
<body>

<section class="card card--front">
  <div class="mascot-art" role="img" aria-label="Cartoon mascot of a doctor with a stethoscope"></div>
  <p class="brand-name">Portal Panel Medic</p>
  <div class="tagline-band"><p class="tagline">Expert Service at an affordable price</p></div>
</section>

<section class="card card--back">
  <div class="mascot-art" role="img" aria-label="Cartoon mascot of a doctor with a stethoscope"></div>
  <p class="brand-name">Portal Panel Medic</p>
  <div class="divider"></div>
  <div class="person">
    <p class="person__name">NAME</p>
    <p class="person__role">Designation</p>
  </div>
  <ul class="contact-list">
    <li>
      <svg viewBox="0 0 14 14"><circle cx="7" cy="7" r="7" fill="var(--accent-red)"/><path d="M4 5.2c0-.8.7-1.2 3-1.2s3 .4 3 1.2v.6H8.6v-.6H5.4v.6H4z M4.6 6.4h4.8l.6 3.6H4z" fill="#fff"/></svg>
      <span>(317) 555-0148</span>
    </li>
    <li>
      <svg viewBox="0 0 14 14"><circle cx="7" cy="7" r="7" fill="var(--accent-red)"/><g fill="none" stroke="#fff" stroke-width="0.9"><circle cx="7" cy="7" r="4"/><ellipse cx="7" cy="7" rx="1.8" ry="4"/><path d="M3 7h8M3.6 5h6.8M3.6 9h6.8"/></g></svg>
      <span>Website</span>
    </li>
    <li>
      <svg viewBox="0 0 14 14"><circle cx="7" cy="7" r="7" fill="var(--accent-red)"/><rect x="3.5" y="4.5" width="7" height="5" fill="#fff"/><path d="M3.5 4.5L7 7.4l3.5-2.9" fill="none" stroke="var(--accent-red)" stroke-width="0.9"/></svg>
      <span>Email</span>
    </li>
  </ul>
</section>

</body>
</html>
```